Need FaceBook, Linkedin, Instagram, Twitter banners designed

We need to have the logos brimlo wallet logo, and the ParcelNote a service of brimlo Logo. Both attached herein. turned into Social Media Banners. (FaceBook, LinkedIn, Instagram, Twitter). Different Banners for each of the two logos for each of the 4 media outlets:
1) brimlo - Just the wallet
2) ParcelNote

```html
<!DOCTYPE html>
<html lang="en">
<head>
<meta charset="utf-8">
<title>brimlo and ParcelNote social banners</title>
<link rel="stylesheet" href="https://fonts.googleapis.com/css2?family=Questrial&display=swap">
<style>
  :root {
    --backdrop: #e4e4e4;
    --card: #ffffff;
    --ink: #2b2b2b;
    --name-grey: #4b4548;
    --wave-cream: #fdf1d8;
    --wave-yellow: #f7c548;
    --wave-orange: #ee8a1c;
    --wave-deep: #c8481a;
    --wave-red: #c41e12;
  }
  * { box-sizing: border-box; margin: 0; padding: 0; }
  html, body {
    width: 1200px;
    height: 848px;
    overflow: hidden;
  }
  body {
    position: relative;
    background: var(--backdrop);
    font-family: "Questrial", "Century Gothic", sans-serif;
  }
  .banner {
    position: absolute;
    background: var(--card);
    overflow: hidden;
  }

  /* brimlo banner */
  .banner--brimlo {
    left: 86px;
    top: 116px;
    width: 653px;
    height: 340px;
  }
  .banner__waves--brimlo {
    position: absolute;
    inset: 0;
    background:
      linear-gradient(168deg,
        var(--card) 0%,
        var(--wave-cream) 22%,
        var(--wave-yellow) 45%,
        var(--card) 55%,
        var(--wave-orange) 70%,
        var(--wave-deep) 88%,
        var(--wave-orange) 100%);
    opacity: 0.9;
  }
  .brand-name {
    position: absolute;
    left: 92px;
    top: 138px;
    font-size: 74px;
    line-height: 1;
    color: var(--name-grey);
    letter-spacing: -1px;
  }

  /* ParcelNote banner */
  .banner--parcelnote {
    left: 462px;
    top: 395px;
    width: 651px;
    height: 341px;
  }
  .service-title {
    position: absolute;
    left: 220px;
    top: 40px;
    color: var(--ink);
  }
  .service-title__name {
    font-size: 52px;
    line-height: 1;
    letter-spacing: -0.5px;
  }
  .service-title__tagline {
    margin-top: 14px;
    font-size: 24px;
    line-height: 1;
    letter-spacing: 1px;
  }
  .banner__waves--parcelnote {
    position: absolute;
    left: 0;
    right: 0;
    bottom: 0;
    height: 260px;
    background:
      linear-gradient(172deg,
        rgba(255,255,255,0) 0%,
        rgba(255,255,255,0) 35%,
        var(--wave-cream) 48%,
        var(--wave-yellow) 62%,
        var(--wave-orange) 74%,
        var(--wave-red) 82%,
        var(--wave-orange) 90%,
        var(--wave-yellow) 100%);
  }
</style>
</head>
<body>
  <section class="banner banner--brimlo" aria-label="brimlo banner">
    <div class="banner__waves banner__waves--brimlo" role="img" aria-label="Flowing orange and gold ribbon waves across the banner"></div>
    <p class="brand-name">brimlo</p>
  </section>

  <section class="banner banner--parcelnote" aria-label="ParcelNote banner">
    <div class="banner__waves banner__waves--parcelnote" role="img" aria-label="Sweeping yellow, orange and red curved bands along the lower edge"></div>
    <div class="service-title">
      <p class="service-title__name">ParcelNote</p>
      <p class="service-title__tagline">a brimlo service</p>
    </div>
  </section>
</body>
</html>
```